Rings and things/plans. Wedding planning checklist design

We are a wedding videography start-up that's about to launch a chatterly campaign. We need a simple yet premium looking design to showcase a wedding planning checklist which we have written. The main focus of the design should be:

- On A4 pages
- Appeal to young engaged women
- Anyone at home can print it off and stick it onto a fridge
- Premium looking

The contents doesn't have to be on one piece of A4, the list can span more than one page. Also, it doesn't have to be traditional folded brochure style, a full A4 sized list is preferred. The design will potentially be used in further A4 brochure style blog posts. The written checklist and our company logo is attached for reference.

Target Market(s)

Young engaged woman

Industry/Entity Type

Wedding

Requirements
Must have
• Simple and premium feel.
Nice to have
• flexible design that can be reused in the future for blog posts.

```html
<!DOCTYPE html>
<html lang="en">
<head>
<meta charset="utf-8">
<title>The Complete Wedding Planning Checklist</title>
<link rel="stylesheet" href="https://fonts.googleapis.com/css2?family=Great+Vibes&family=Josefin+Sans:wght@400;600&family=Lato:wght@400;700&family=Tinos:wght@700&display=swap">
<style>
  :root {
    --stage: #e9e7e4;
    --charcoal: #2e2e2e;
    --charcoal-deep: #1f1f1f;
    --paper: #ffffff;
    --paper-shade: #eeeeee;
    --swoosh: #dcdcdc;
    --ink: #1d1d1d;
    --ink-soft: #2b2b2b;
    --sky: #c9dcef;
    --sea: #8fb8c9;
    --sand: #e7ddd0;
    --white: #ffffff;
  }
  * { margin: 0; padding: 0; box-sizing: border-box; }
  html, body { width: 907px; height: 1200px; overflow: hidden; }
  body { background: var(--stage); position: relative; }

  .flyer {
    position: absolute;
    left: 39px; top: 20px;
    width: 828px; height: 1160px;
    overflow: hidden;
    background: var(--paper);
    box-shadow: 0 4px 18px rgba(0,0,0,.18);
  }
  .flyer-shapes { position: absolute; inset: 0; }

  .cover-title {
    position: absolute;
    left: 40px; top: 98px;
    width: 300px;
    text-align: center;
    color: var(--ink-soft);
  }
  .cover-title .lead {
    font-family: "Josefin Sans", sans-serif;
    font-size: 34px; line-height: 44px;
  }
  .cover-title .script {
    font-family: "Great Vibes", cursive;
    font-size: 78px; line-height: 76px;
    color: var(--white);
    text-shadow: 0 2px 4px rgba(0,0,0,.35);
  }
  .cover-title .script.dark { color: var(--ink); text-shadow: none; }
  .cover-title .caps {
    font-family: "Josefin Sans", sans-serif;
    font-weight: 600;
    font-size: 28px; letter-spacing: 1px;
    margin-top: 10px;
  }

  .brand {
    position: absolute; left: 0; right: 0; top: 684px;
    text-align: center;
    font-family: "Lato", sans-serif; font-weight: 400;
    font-size: 42px; line-height: 50px;
    color: var(--ink);
  }

  .intro {
    position: absolute; left: 0; right: 0; top: 800px;
    text-align: center; color: var(--ink);
  }
  .intro-title {
    font-family: "Tinos", serif; font-weight: 700;
    font-size: 33px;
  }
  .intro-sub {
    font-family: "Lato", sans-serif;
    font-size: 27px; margin-top: 4px; color: var(--ink-soft);
  }
  .author {
    font-family: "Lato", sans-serif; font-weight: 700;
    font-size: 21px; line-height: 29px; margin-top: 14px;
  }
  .contact {
    font-family: "Lato", sans-serif;
    font-size: 22px; margin-top: 28px;
  }

  .footer {
    position: absolute; left: 0; right: 0; top: 1098px;
    display: flex; align-items: center; justify-content: center; gap: 14px;
    font-family: "Lato", sans-serif; font-size: 19px;
    color: var(--white);
  }
  .social { display: flex; align-items: center; gap: 6px; font-size: 15px; }
  .social::before {
    content: ""; width: 10px; height: 10px; border-radius: 50%;
    background: var(--white);
  }
</style>
</head>
<body>
  <main class="flyer">
    <svg class="flyer-shapes" viewBox="0 0 828 1160" width="828" height="1160">
      <defs>
        <linearGradient id="photoTone" x1="0" y1="0" x2="0" y2="1">
          <stop offset="0" stop-color="var(--sky)"/>
          <stop offset=".45" stop-color="var(--sea)"/>
          <stop offset="1" stop-color="var(--sand)"/>
        </linearGradient>
        <linearGradient id="paperTone" x1="0" y1="0" x2="0" y2="1">
          <stop offset="0" stop-color="var(--paper)"/>
          <stop offset="1" stop-color="var(--paper-shade)"/>
        </linearGradient>
      </defs>
      <rect class="cover-photo" x="0" y="0" width="828" height="660" fill="url(#photoTone)"
            role="img" aria-label="Photograph of a smiling bride in a veil and groom embracing by the sea"/>
      <path class="band-top" d="M0,491 Q414,701 828,491 L828,1160 L0,1160 Z" fill="var(--charcoal)"/>
      <path class="swoosh-top" d="M0,534 Q414,678 828,534" fill="none" stroke="var(--swoosh)" stroke-width="6"/>
      <path class="paper-panel" d="M0,545 Q414,688 828,545 L828,1160 L0,1160 Z" fill="url(#paperTone)"/>
      <path class="swoosh-bottom" d="M0,905 Q414,1210 828,905" fill="none" stroke="var(--swoosh)" stroke-width="8"/>
      <path class="band-bottom" d="M0,927 Q414,1235 828,927 L828,1160 L0,1160 Z" fill="var(--charcoal-deep)"/>
    </svg>

    <header class="cover-title">
      <p class="lead">~ The ~</p>
      <p class="lead">complete</p>
      <p class="script">Wedding</p>
      <p class="script dark">Planning</p>
      <p class="caps">CHECKLIST</p>
    </header>

    <p class="brand">Amber &amp; Oak</p>

    <section class="intro">
      <h1 class="intro-title">~ The Ultimate Wedding Planning Checklist ~</h1>
      <p class="intro-sub">Rings and plans!</p>
      <p class="author">Written by Mara Lindell<br>Wedding Planner</p>
      <p class="contact">maralindell@example.com</p>
    </section>

    <footer class="footer">
      <span>Connect with Us</span>
      <span class="social">chatterly</span>
      <span class="social">Pinboardly</span>
      <span class="social">Chirpline</span>
    </footer>
  </main>
</body>
</html>
```